K & D A/C Compressors' Business Card

Hello,

I need someone to create a new business card for my business. The name of my Business is: K & D A/C Compressors. I sell automotive air conditioning parts (a/c parts). I would like the business card to incorporate my logo, and to have an automotive feel to it. It is important that the business card feel like it is coming from an automotive parts business.

I already have a logo, which I will provide.

Thanks.
Updates

Project Deadline Extended Reason: I feel like extending the deadline until October 9, 2017, will allow for more time to design the business card. Thank you for your understanding. Added Monday, October 2, 2017

Target Market(s)

Consumers who need automotive a/c parts, and auto mechanics.

Industry/Entity Type

Automotive

Contact Information for Business Card

Business name: K & D A/C Compressors
Business Address: 48207 Southwest 36th Street, North Miami Beach, Florida 33162
Telephone: 305-472-1390
Fax: To be provided once I choose your design.
Website: www.kdcoolunits.example
Email: support@kdcoolunits.example
Names: To be provided once I choose your design.

Font styles to use
Sans Serif

Colors

Designer to choose colors to be used in the design.

Requirements
Must have
• The business card must include all of the "Business Card Details" and the logo I have uploaded.

```html
<!DOCTYPE html>
<html lang="en">
<head>
<meta charset="utf-8">
<title>K &amp; D A/C Compressors – Business Card</title>
<link href="https://fonts.googleapis.com/css2?family=Open+Sans:wght@400;600;700&display=swap" rel="stylesheet">
<style>
  :root {
    --bg: #5d5d5d;
    --brand-blue: #29aae1;
    --card-white: #ffffff;
    --ink: #1a1a1a;
    --muted: #9a9a9a;
    --logo-grey: #a3a3a3;
    --icon-grey: #8c8c8c;
  }
  * { box-sizing: border-box; margin: 0; padding: 0; }
  html, body {
    width: 1200px; height: 1200px; overflow: hidden;
    background: var(--bg);
    font-family: "Open Sans", Arial, sans-serif;
  }
  .sheet {
    width: 1200px; height: 1200px;
    display: flex; align-items: center; justify-content: center; gap: 16px;
  }
  .card {
    position: relative;
    width: 560px; height: 314px;
    overflow: hidden;
  }
  .card--front { background: var(--card-white); }
  .card--back { background: var(--brand-blue); }

  .brand-name {
    position: absolute; left: 28px; top: 40px;
    display: flex; align-items: center; gap: 10px;
    font-weight: 600; font-size: 19px; line-height: 1.2;
    color: var(--logo-grey);
    white-space: nowrap;
  }
  .brand-mark { width: 16px; height: 16px; background: var(--brand-blue); flex: none; }

  .person { position: absolute; left: 268px; top: 76px; }
  .person__name { font-weight: 700; font-size: 22px; color: var(--ink); line-height: 1.2; }
  .person__title { font-size: 14px; color: var(--muted); line-height: 1.3; }

  .address {
    position: absolute; left: 28px; top: 184px;
    font-size: 16.5px; line-height: 22px; color: var(--ink);
    font-style: normal;
  }
  .address__company { font-weight: 600; }

  .contacts {
    position: absolute; left: 266px; top: 184px;
    list-style: none;
    font-size: 16.5px; line-height: 22px; color: var(--ink);
  }
  .contacts li { display: flex; align-items: center; gap: 8px; }
  .contacts svg { width: 13px; height: 13px; flex: none; }

  .web-band {
    position: absolute; left: 0; right: 0; bottom: 0; height: 48px;
    background: var(--brand-blue);
    display: flex; align-items: center; justify-content: center;
    color: var(--card-white); font-weight: 700; font-size: 20px;
  }

  .back-brand {
    position: absolute; inset: 0;
    display: flex; align-items: center; justify-content: center; gap: 16px;
    color: var(--card-white); font-weight: 600; font-size: 34px;
    white-space: nowrap;
  }
  .back-brand .brand-mark { width: 26px; height: 26px; background: var(--card-white); }
</style>
</head>
<body>
<main class="sheet">
  <section class="card card--front" aria-label="Business card front">
    <div class="brand-name"><span class="brand-mark"></span><span>K &amp; D A/C Compressors</span></div>

    <div class="person">
      <p class="person__name">Marcus Delane</p>
      <p class="person__title">Support Executive</p>
    </div>

    <address class="address">
      <span class="address__company">K &amp; D A/C Compressors</span><br>
      48207 SW 36th Street<br>
      N. Miami Beach, FL 33179
    </address>

    <ul class="contacts">
      <li>
        <svg viewBox="0 0 16 16" aria-hidden="true"><path d="M4 1.5l2.2 3-1.4 1.6c.8 1.8 2.3 3.3 4.1 4.1l1.6-1.4 3 2.2-1.3 2.6C7.5 13.6 2.4 8.5 1.4 3.8z" fill="var(--icon-grey)"/></svg>
        (305)-472-1390
      </li>
      <li>
        <svg viewBox="0 0 16 16" aria-hidden="true"><rect x="4" y="1.5" width="8" height="5" fill="none" stroke="var(--icon-grey)" stroke-width="1.3"/><rect x="1.5" y="6.5" width="13" height="8" rx="1" fill="none" stroke="var(--icon-grey)" stroke-width="1.3"/><path d="M4 9.5h2M4 11.5h2M8 9.5h4" stroke="var(--icon-grey)" stroke-width="1.2"/></svg>
        (305)-472-1391
      </li>
      <li>
        <svg viewBox="0 0 16 16" aria-hidden="true"><rect x="1.5" y="3.5" width="13" height="9" fill="none" stroke="var(--icon-grey)" stroke-width="1.3"/><path d="M1.5 3.5L8 9l6.5-5.5" fill="none" stroke="var(--icon-grey)" stroke-width="1.3"/></svg>
        support@kdcoolunits.example
      </li>
    </ul>

    <div class="web-band">www.kdcoolunits.example</div>
  </section>

  <section class="card card--back" aria-label="Business card back">
    <div class="back-brand"><span class="brand-mark"></span><span>K &amp; D A/C Compressors</span></div>
  </section>
</main>
</body>
</html>
```